FenderPals Personal Injury Lawyers Website (Wordpress)

We need a brand new website for our firm's new rebranding. The name of the website is www.fenderpals-example.com. Our new brand will be a group of personal injury lawyers focused on representing only victims in car wrecks. We will be distinguishing ourselves from other law firms due to the fact that other law firms represent clients involving all forms of personal injury. We will only focus on car wrecks and this needs to be reflected on the website.

I have attached the new firm logo and stationary to show the designers the kind of look we are going for in the new website. It needs to be clean, pure, and show the potential clients that we only do one thing and we do it well. That thing is car wrecks.

Some examples of websites that we like are the following:
www.qvt-example.lu - nice interface and colors. nice navigation, we really like the biography pages for the individuals attorneys
www.morvantlegal-example.com - good layout, good navigation
www.pelliardwoss-example.com - navigation bar follows the user whether the user goes up or down

We would like five separate pages -- (1) Home, (2) Client Resources, (3) Expertise / Car Wrecks, (4) Contact Us, (5) News

The Home page will be used for driving traffic and should have a call to action on the right at the top stating that we will send an ebook to anyone who gives their contact information. The ebook will explain how car wrecks work. This should also have room for youtube videos which will be added later.

The client resources will include blogs, books, and information for potential clients. It should be presented in a well developed manner which is both appealing to potential and current clients.

The expertise page will show that we only focus on car wrecks. This needs to be a recurrent theme throughout the entire website. This page will focus on car wrecks and the different aspects including damages, insurance, and investigation.

The Contact Us page will show a google map to our address and phone number. Please use generic information and we will fill in the gaps upon the selection.

News: the news page will show different articles related to past and present cases and the successes of those clients.

The overall page should be elegant and creative. Do not include courthouses, gavels or anything else related to the law. If you include these things, your design will automatically be excluded.
Updates

Please take note this design is now guaranteed. I look forward to receiving everyone's wonderful designs.

Target Market(s)

Persons involved in car wrecks

Industry/Entity Type

Legal

Coding

Coded - Design and coding required

Number of Pages Required

5+ page

Font styles to use
Serif
Sans Serif

Colors
ec1f27
ffffff
000000

Requirements
Must have
• Five pages which focus on representation of car wreck victims. The site must be clean and easy to navigate.
Nice to have
• Navigation bar should follow user up and down the page.
Should not have
• Gavels, court houses, anything related to the law. If your design has these aspects, it will automatically be rejected

```html
<!DOCTYPE html>
<html lang="en">
<head>
<meta charset="utf-8">
<title>FenderPals – Personal Injury Lawyers</title>
<link href="https://fonts.googleapis.com/css2?family=Lato:ital,wght@0,400;0,700;0,900;1,400&family=Open+Sans:wght@400;600&display=swap" rel="stylesheet">
<style>
:root{
  --red:#ec1f27;
  --black:#000000;
  --ink:#222222;
  --charcoal:#2b2b2b;
  --charcoal-2:#1f1f1f;
  --grey-text:#666666;
  --grey-light:#f1f1f1;
  --line:#dddddd;
  --white:#ffffff;
}
*{box-sizing:border-box;margin:0;padding:0}
html,body{width:1200px;height:2292px;overflow:hidden}
body{font-family:"Open Sans",Arial,sans-serif;color:var(--ink);background:var(--white);font-size:12px;line-height:1.6}
.wrap{width:1000px;margin:0 auto;position:relative;height:100%}
h1,h2,h3,h4,.nav{font-family:"Lato",Arial,sans-serif}

/* header */
.site-header{height:96px}
.brand{position:absolute;left:0;top:26px;display:flex;align-items:center;gap:12px}
.brand-mark{width:34px;height:34px;background:var(--red)}
.brand-name{font-family:"Open Sans",Arial,sans-serif;font-size:30px;font-weight:600;color:var(--ink);line-height:1}
.brand-tag{font-size:12px;color:var(--grey-text);margin-top:4px}
.call{position:absolute;right:0;top:24px;display:flex;align-items:center;gap:10px}
.call-icon{width:40px;height:40px;border-radius:50%;background:var(--red);display:flex;align-items:center;justify-content:center}
.call-label{font-size:11px;color:var(--grey-text);line-height:1.1}
.call-number{font-family:"Lato",sans-serif;font-size:22px;font-weight:700;color:var(--red);line-height:1.1}

/* nav */
.nav{height:44px;background:var(--charcoal)}
.nav .wrap{display:flex;align-items:stretch}
.nav a{color:var(--white);text-decoration:none;font-size:12px;font-weight:700;letter-spacing:.5px;display:flex;align-items:center;padding:0 20px}
.nav a.active{background:var(--red)}
.nav .nav-extra{margin-left:auto;background:var(--charcoal-2);padding:0 26px}

/* hero */
.hero{height:420px;position:relative;overflow:hidden}
.hero-photo{position:absolute;inset:0;background:linear-gradient(100deg,#5a5a5c 0%,#8e8f93 35%,#c9c9cb 55%,#3d3e42 80%,#1c1c1e 100%)}
.hero-headline{position:absolute;left:100px;top:246px;color:var(--white);font-size:32px;font-weight:700;line-height:1.2;text-shadow:0 1px 3px rgba(0,0,0,.4)}
.hero-band{position:absolute;left:0;top:326px;height:40px;width:620px;background:var(--red);color:var(--white);font-style:italic;font-size:16px;display:flex;align-items:center;padding-left:100px;opacity:.92}
.hero-cta{position:absolute;right:100px;top:310px;height:70px;width:340px;background:rgba(0,0,0,.8);display:flex;align-items:center;gap:14px;padding-left:24px;color:var(--white);font-family:"Lato",sans-serif;font-size:26px;font-weight:700}
.hero-strip{position:absolute;left:0;right:0;bottom:0;height:40px;background:rgba(0,0,0,.75)}

/* headings */
.section-title{font-size:26px;font-weight:900;color:var(--ink);text-transform:uppercase}
.section-title span{color:var(--red)}
.rule{width:60px;height:3px;background:var(--red);margin:8px 0 16px}
.btn{display:inline-block;background:var(--red);color:var(--white);font-size:11px;font-weight:600;padding:5px 14px;text-decoration:none}
.btn.ghost{background:transparent;border:1px solid var(--white)}

/* welcome */
.welcome{height:360px;padding-top:40px}
.welcome-text{position:absolute;left:0;top:0;width:560px}
.welcome-text p{color:var(--grey-text);margin-bottom:12px;font-size:11.5px}
.video{position:absolute;right:0;top:0;width:400px;height:250px;background:linear-gradient(135deg,#7d8792,#c7cbd0 50%,#5b6068);display:flex;align-items:center;justify-content:center}
.video-dots{position:absolute;right:0;top:262px;width:400px;display:flex;justify-content:center;gap:8px}
.video-dots i{width:9px;height:9px;border-radius:50%;background:var(--line)}
.video-dots i.on{background:var(--red)}

/* expertise */
.expertise{height:470px;position:relative;display:flex}
.expertise-photo{position:absolute;inset:0;background:linear-gradient(90deg,#6e6e70,#b0b0b2 45%,#2a2a2c 55%,#111 100%)}
.expertise-left{position:relative;width:600px;background:rgba(236,31,39,.88);color:var(--white);padding:80px 60px 0 100px}
.expertise-left h2{font-size:28px;font-weight:900;text-transform:uppercase}
.expertise-left .rule{background:var(--white)}
.expertise-left p{font-size:15px;line-height:1.5;margin-bottom:18px;opacity:.95}
.expertise-right{position:relative;width:600px;background:rgba(20,20,20,.88);padding:80px 100px 0 60px}
.topic{display:flex;gap:18px;margin-bottom:40px;color:var(--white)}
.topic-icon{flex:0 0 52px;height:52px;border-radius:50%;background:var(--white);display:flex;align-items:center;justify-content:center}
.topic h3{font-size:16px;font-weight:900;letter-spacing:.5px}
.topic p{font-size:11px;color:#cfcfcf}

/* news */
.news{height:340px;padding-top:40px}
.news .section-title{text-align:center}
.news .rule{margin:8px auto 34px}
.news-grid{display:flex}
.news-item{flex:1;display:flex;gap:14px;padding:0 20px;border-left:1px solid var(--line)}
.news-item:first-child{border-left:none;padding-left:0}
.date{flex:0 0 56px;height:92px;border:1px solid var(--line);text-align:center}
.date b{display:block;font-family:"Lato",sans-serif;font-size:24px;color:var(--ink);line-height:40px}
.date span{display:block;background:var(--red);color:var(--white);font-size:11px;font-weight:600}
.news-item h4{color:var(--red);font-size:13px;line-height:1.3;margin-bottom:6px}
.news-item p{font-size:11px;color:var(--grey-text)}

/* posts + testimonials */
.feature{height:350px;background:var(--grey-light);padding-top:34px}
.col{position:absolute;top:0;width:480px}
.col.right{right:0}
.col-head{display:flex;justify-content:space-between;align-items:center;border-bottom:2px solid var(--line);padding-bottom:6px;margin-bottom:22px}
.col-head h2{font-size:20px;font-weight:900;text-transform:uppercase}
.col-head h2 span{color:var(--red)}
.view-all{font-size:10px;border:1px solid #bbb;padding:2px 8px;color:var(--grey-text)}
.post{display:flex;gap:14px;margin-bottom:24px}
.post-thumb{flex:0 0 120px;height:86px;background:linear-gradient(135deg,#4b6b93,#b8c4d2 55%,#2f3b4c)}
.post h4{color:var(--red);font-size:12px;line-height:1.3}
.post .meta{font-size:10px;color:#999;margin:3px 0}
.post p{font-size:11px;color:var(--grey-text)}
.testimonial{display:flex;gap:20px}
.avatar{flex:0 0 110px;height:110px;border-radius:50%;background:linear-gradient(#9aa3ad,#5d656e);border:4px solid var(--white)}
.quote-mark{color:var(--red);font-family:Georgia,serif;font-size:36px;line-height:.6;font-weight:700}
.testimonial p{font-size:12px;color:var(--grey-text);margin:6px 0 10px}
.testimonial cite{font-size:11px;color:var(--ink);font-style:italic}

/* footer */
.site-footer{height:212px;background:var(--charcoal);color:#cfcfcf;padding-top:24px}
.f-col{position:absolute;top:0}
.f-col h4{color:var(--white);font-size:13px;font-weight:900;text-transform:uppercase;margin-bottom:12px}
.field{width:240px;height:20px;background:var(--white);margin-bottom:6px;font-size:10px;color:#999;padding:2px 6px}
.field.tall{height:30px}
.submit{display:inline-block;background:var(--red);color:var(--white);font-size:10px;padding:3px 12px}
.news-form{display:flex;margin-top:12px}
.news-form .field{width:200px;margin:0}
.news-form .submit{padding:3px 10px;line-height:14px}
.find li{list-style:none;display:flex;gap:10px;align-items:flex-start;font-size:11px;margin-bottom:10px}
.find .fi{flex:0 0 22px;height:22px;border-radius:50%;background:var(--red);display:flex;align-items:center;justify-content:center}
.follow{position:absolute;left:340px;top:152px;display:flex;align-items:center;gap:8px;color:var(--white);font-family:"Lato",sans-serif;font-weight:900;font-size:13px}
.follow i{width:22px;height:22px;border-radius:50%;background:#e6e6e6;display:inline-block}
.copy{position:absolute;right:0;top:160px;font-size:10px;color:#999}
</style>
</head>
<body>

<header class="site-header">
  <div class="wrap">
    <div class="brand">
      <span class="brand-mark"></span>
      <div>
        <div class="brand-name">FenderPals</div>
        <div class="brand-tag">Personal Injury Lawyers</div>
      </div>
    </div>
    <div class="call">
      <div class="call-icon">
        <svg width="20" height="20" viewBox="0 0 24 24"><path fill="#fff" d="M6.6 10.8c1.4 2.8 3.8 5.1 6.6 6.6l2.2-2.2c.3-.3.7-.4 1-.2 1.1.4 2.3.6 3.6.6.6 0 1 .4 1 1V20c0 .6-.4 1-1 1C10.6 21 3 13.4 3 4c0-.6.4-1 1-1h3.5c.6 0 1 .4 1 1 0 1.3.2 2.5.6 3.6.1.3 0 .7-.2 1l-2.3 2.2z"/></svg>
      </div>
      <div>
        <div class="call-label">Call Today</div>
        <div class="call-number">123-456-7890</div>
      </div>
    </div>
  </div>
</header>

<nav class="nav">
  <div class="wrap">
    <a class="active">HOME</a>
    <a>CLIENT RESOURCES</a>
    <a>EXPERTISE / CAR WRECKS</a>
    <a>NEWS</a>
    <a>CONTACT US</a>
    <a class="nav-extra">HOW CAR WRECKS WORK &nbsp;▾</a>
  </div>
</nav>

<section class="hero">
  <div class="hero-photo" role="img" aria-label="Photo of a damaged car after a collision with a distressed driver beside it"></div>
  <h1 class="hero-headline">We understand the stress<br>your disability causes.</h1>
  <div class="hero-band">We know that you need your benefits as soon as possible.</div>
  <div class="hero-cta">
    <svg width="40" height="40" viewBox="0 0 40 40"><path fill="none" stroke="#fff" stroke-width="2.5" d="M4 9c6-2 11-1 16 3 5-4 10-5 16-3v23c-6-2-11-1-16 3-5-4-10-5-16-3z M20 12v23"/></svg>
    Get A Free Book
  </div>
  <div class="hero-strip"></div>
</section>

<section class="welcome">
  <div class="wrap">
    <div class="welcome-text">
      <h2 class="section-title">Welcome to FenderPals</h2>
      <div class="rule"></div>
      <p>After a car wreck you deserve a team that handles nothing else. We guide victims through medical bills, insurance calls and repair claims so you can focus fully on healing. Every case we take is a car wreck, and every hour we spend sharpens the way we fight for our clients in and out of negotiations with the insurers.</p>
      <p>Our lawyers meet you quickly, listen closely and build a clear plan for your claim. We gather police reports, photos, witness statements and medical records, then push for a fair result without delay. You pay nothing unless we recover money for you.</p>
      <a class="btn">Read More</a>
    </div>
    <div class="video" role="img" aria-label="Video player placeholder showing a driver speaking with a lawyer">
      <svg width="64" height="44" viewBox="0 0 64 44"><rect width="64" height="44" rx="8" fill="rgba(0,0,0,.6)"/><path d="M26 12l16 10-16 10z" fill="#fff"/></svg>
    </div>
    <div class="video-dots"><i class="on"></i><i></i><i></i></div>
  </div>
</section>

<section class="expertise">
  <div class="expertise-photo" role="img" aria-label="Photo of a wrecked car at a crash scene"></div>
  <div class="expertise-left">
    <h2>Expertise / Car Wrecks</h2>
    <div class="rule"></div>
    <p>Car wrecks are the only cases we handle. That single focus means deeper knowledge, faster answers and stronger results for every client we represent after a crash.</p>
    <a class="btn ghost">Read More</a>
  </div>
  <div class="expertise-right">
    <div class="topic">
      <div class="topic-icon"><svg width="26" height="26" viewBox="0 0 24 24"><path d="M12 3l10 18H2z" fill="none" stroke="#ec1f27" stroke-width="2.2"/><path d="M12 10v5M12 17v1.5" stroke="#ec1f27" stroke-width="2.2"/></svg></div>
      <div><h3>DAMAGES</h3><p>We document every loss, from medical costs and lost wages to pain and vehicle repair, so nothing is left out.</p></div>
    </div>
    <div class="topic">
      <div class="topic-icon"><svg width="26" height="26" viewBox="0 0 24 24"><path d="M12 2l8 3v6c0 5-3.5 9-8 11-4.5-2-8-6-8-11V5z" fill="none" stroke="#ec1f27" stroke-width="2.2"/><path d="M8 12l3 3 5-6" fill="none" stroke="#ec1f27" stroke-width="2.2"/></svg></div>
      <div><h3>INSURANCE</h3><p>We deal with the adjusters for you and press for the full value your policy and the law allow.</p></div>
    </div>
    <div class="topic">
      <div class="topic-icon"><svg width="26" height="26" viewBox="0 0 24 24"><circle cx="10" cy="10" r="6" fill="none" stroke="#ec1f27" stroke-width="2.2"/><path d="M14.5 14.5L21 21" stroke="#ec1f27" stroke-width="2.6"/></svg></div>
      <div><h3>INVESTIGATION</h3><p>We study the scene, reports and witnesses to prove exactly how the wreck happened and who caused it.</p></div>
    </div>
  </div>
</section>

<section class="news">
  <div class="wrap">
    <h2 class="section-title">Latest <span>News</span></h2>
    <div class="rule"></div>
    <div class="news-grid">
      <article class="news-item">
        <div class="date"><b>22</b><span>Aug</span></div>
        <div><h4>Client wins full recovery after highway crash claim</h4><p>A rear end collision left our client with months of therapy. We secured payment for every bill and lost wage.</p></div>
      </article>
      <article class="news-item">
        <div class="date"><b>15</b><span>June</span></div>
        <div><h4>New guide explains your first steps after a wreck</h4><p>Our free ebook walks you through reports, photos, doctors and insurers in plain and simple language.</p></div>
      </article>
      <article class="news-item">
        <div class="date"><b>10</b><span>May</span></div>
        <div><h4>Settlement reached for family hit at busy crossing</h4><p>After a careful investigation the driver at fault accepted blame and the family received fair compensation.</p></div>
      </article>
    </div>
  </div>
</section>

<section class="feature">
  <div class="wrap">
    <div class="col">
      <div class="col-head"><h2>Latest <span>Post</span></h2><span class="view-all">View All</span></div>
      <div class="post">
        <div class="post-thumb" role="img" aria-label="Photo of police at a car crash scene"></div>
        <div><h4>What to do in the first hour after a car wreck</h4><div class="meta">Posted by Admin · 12 Comments</div><p>Stay safe, call for help, take photos and trade details. These steps protect your health and your claim later.</p></div>
      </div>
      <div class="post">
        <div class="post-thumb" role="img" aria-label="Photo of two damaged cars on a road"></div>
        <div><h4>How insurers value your injury claim today</h4><div class="meta">Posted by Admin · 8 Comments</div><p>Learn what adjusters look at, why records matter and how early advice can raise the value of your case.</p></div>
      </div>
    </div>
    <div class="col right">
      <div class="col-head"><h2>Client <span>Testimonials</span></h2><span class="view-all">View All</span></div>
      <div class="testimonial">
        <div class="avatar" role="img" aria-label="Client portrait placeholder"></div>
        <div>
          <div class="quote-mark">“</div>
          <p>After my crash I had no idea where to start. The team took every call, explained each step and won a result I never expected. I could rest and heal while they handled the insurers for me from start to finish.</p>
          <div class="quote-mark" style="text-align:right">”</div>
          <cite>Mr. Daniel Hart</cite>
        </div>
      </div>
    </div>
  </div>
</section>

<footer class="site-footer">
  <div class="wrap">
    <div class="f-col" style="left:0">
      <h4>Quick Contact</h4>
      <div class="field">Name</div>
      <div class="field">Email</div>
      <div class="field">Phone</div>
      <div class="field tall">Message</div>
      <span class="submit">Submit</span>
    </div>
    <div class="f-col" style="left:340px">
      <h4>Newsletter Signup</h4>
      <p style="font-size:11px;width:200px">Get the latest updates by entering your email address</p>
      <svg style="position:absolute;left:240px;top:24px" width="44" height="34" viewBox="0 0 44 34"><path d="M2 16L42 2 32 32 20 20z" fill="#cfcfcf"/><path d="M20 20L42 2" stroke="#2b2b2b" stroke-width="1.5"/></svg>
      <div class="news-form"><div class="field">Enter your email here</div><span class="submit">Subscribe</span></div>
    </div>
    <div class="f-col find" style="left:720px;width:280px">
      <h4>Find Us</h4>
      <ul>
        <li><span class="fi"><svg width="12" height="12" viewBox="0 0 24 24"><path fill="#fff" d="M12 2a7 7 0 017 7c0 5-7 13-7 13S5 14 5 9a7 7 0 017-7zm0 4a3 3 0 100 6 3 3 0 000-6z"/></svg></span>100 Main Street, Suite 200<br>Anytown, State 00000</li>
        <li><span class="fi"><svg width="12" height="12" viewBox="0 0 24 24"><path fill="#fff" d="M6.6 10.8c1.4 2.8 3.8 5.1 6.6 6.6l2.2-2.2c.3-.3.7-.4 1-.2 1.1.4 2.3.6 3.6.6.6 0 1 .4 1 1V20c0 .6-.4 1-1 1C10.6 21 3 13.4 3 4c0-.6.4-1 1-1h3.5c.6 0 1 .4 1 1 0 1.3.2 2.5.6 3.6.1.3 0 .7-.2 1z"/></svg></span>123-456-7890</li>
        <li><span class="fi"><svg width="12" height="12" viewBox="0 0 24 24"><path fill="#fff" d="M2 5h20v14H2z"/><path d="M2 5l10 8 10-8" fill="none" stroke="#ec1f27" stroke-width="2"/></svg></span>info@fenderpals-example.com</li>
      </ul>
    </div>
    <div class="follow">FOLLOW US <i></i><i></i><i></i><i></i></div>
    <div class="copy">Copyright © 2024 FenderPals. All Rights Reserved.</div>
  </div>
</footer>

</body>
</html>
```